Vossmer Collective - Business Card Design

several yrs ago
i have been one of the top 40 pellham photographers

when my fellow photo friends tried to join Pellham Visuals they were all rejected

Pellham Visuals told me if i formed some type of umbrella company of selected photographers they would offer me a contract as long as the portfolio images are stock worthy

so-i started the Vossmer Collective originally just for my friends and family and then grow the company to a few hundred photographers

after 4 yrs of working out all the bugs out
i will be offering other photographers to join the Vossmer Collective
------------

I now need a pro business card — retina website — an info pack about the Vossmer Collective

i bought the logo design from — https://www.markfoundry-example.com

i look at this logo as a group of independent silver balls with orange balls forming a larger group
- the Vossmer Collective
a group of independent members that will have their images sold thru Pellham Visuals - the worlds largest stack agency — under the Vossmer Collective name
--------

the look of the shadows and highlights in the logo

I want the fonts to have the similar look when it works

use the exact shade of orange and silver
I would like another to be the minor color ?

a contributor to Pellham Visuals - i want to really communicate this info
it makes my no name bus into something

please do not continue with this project

this project is on hold

in no order - information that should be part of the design - the most important part of the card - the bus name - VOSSMER COLLECTIVE - under Vossmer Collective you should have a creative tag line A contributor to Pellham Visuals - i like to see a 3d effect - refer to the website where i bought the logo - https://www.markfoundry-example.com - i included the Brink font that we used for the Vossmer Collective - incorporate this only if it helps the design - card stock - please include something other than wht - i have always liked a subtle translucent for background - only horizontal designs - one side of the card should have the logo and tag line together - use the symbols for phone mail etc.. - note the " i " in Vossmer Collective should be the same shade of orange - my card should have on this info - morris vossmer /founder / 717 555 0143 / website / email other card - tessa orbanek - her info is in the orig brief

Reason: this is my first time i have used a online site for design - only a few of the designs have the correct info none of the designs used the font that was included “brink” no one submitted a 3d feel to the designs - i need the card to have that Wow effect I just sent a more detailed brief to everyone thank you morris

Please - No more submissions

Target Market(s)

pro photographers and enthusiast

Industry/Entity Type

Business

Contact Information for Business Card

1. morris vossmer / founder -
2. tessa orbanek - 3. leon taverly
- i will add more names later

company - VOSSMER collective - tag line under logo? - in a script font - " a contributor to pellham visuals"

1. mv - no address for me

2. to - 418 E. 7th Street. Lower Marsden, NJ 08519. 609.555.0187. orbanek@inboxmail-example.com

I have several examples of what we started using their templates

Requirements
Must have
• the shadows and highlights in the logo

fonts to have the similar look when it works

Another color to be a minor color ?

i want this phrase to be included in the company name — "a contributor to Pellham Visuals"

it needs to be next to — floating around the logo — under the Vossmer Collective name anyway connecting it to the Vossmer Collective name
Nice to have
• i hope the folder names are somewhere attached to each file - if not - i will need review each file so you can understand what folder they belong to make sense of each file

i hope you get what i am trying to say
Should not have
• no address for morris vossmer

```html
<!DOCTYPE html>
<html lang="en">
<head>
<meta charset="utf-8">
<title>Vossmer Collective – Business Card</title>
<link href="https://fonts.googleapis.com/css2?family=Michroma&family=Questrial&display=swap" rel="stylesheet">
<style>
  :root {
    --stage: #3b3b3d;
    --silver-light: #f4f4f4;
    --silver-mid: #d2d2d3;
    --silver-dark: #a9a9ab;
    --ink: #5b5e63;
    --orange: #e2521f;
    --orange-deep: #c9321c;
    --white: #ffffff;
  }
  * { box-sizing: border-box; margin: 0; padding: 0; }
  html, body { width: 1200px; height: 900px; overflow: hidden; }
  body {
    background: var(--stage);
    font-family: "Questrial", Arial, sans-serif;
    position: relative;
  }
  .card {
    position: absolute;
    left: 250px;
    width: 700px;
    height: 400px;
    border-radius: 18px;
    overflow: hidden;
    background: linear-gradient(160deg, var(--silver-light) 0%, var(--silver-mid) 55%, var(--silver-dark) 100%);
    box-shadow: 0 14px 30px rgba(0,0,0,.45);
  }
  .card--back { top: 40px; }
  .card--front { top: 470px; }

  /* brand lock-up */
  .brand {
    position: absolute;
    display: flex;
    align-items: center;
    gap: 14px;
    font-family: "Michroma", Arial, sans-serif;
    color: var(--ink);
  }
  .brand__dot {
    border-radius: 50%;
    background: var(--orange);
    flex: none;
  }
  .brand__name { display: flex; flex-direction: column; line-height: 1; }
  .brand__title { letter-spacing: 1px; white-space: nowrap; }
  .brand__sub { align-self: flex-end; letter-spacing: 2px; margin-top: 6px; white-space: nowrap; }

  .card--back .brand { left: 50%; top: 120px; transform: translateX(-50%); }
  .card--back .brand__dot { width: 44px; height: 44px; }
  .card--back .brand__title { font-size: 54px; }
  .card--back .brand__sub { font-size: 18px; }
  .tagline {
    position: absolute;
    left: 0; right: 0;
    top: 262px;
    text-align: center;
    color: var(--orange);
    font-size: 19px;
    letter-spacing: 6px;
  }

  /* front */
  .front-art { position: absolute; inset: 0; }
  .card--front .brand { left: 110px; top: 70px; }
  .card--front .brand__dot { width: 26px; height: 26px; }
  .card--front .brand__title { font-size: 30px; }
  .card--front .brand__sub { font-size: 11px; }

  .contacts {
    position: absolute;
    left: 22px;
    top: 200px;
    list-style: none;
    display: flex;
    flex-direction: column;
    gap: 12px;
  }
  .contact { display: flex; align-items: center; height: 30px; }
  .contact__tab {
    width: 36px; height: 30px;
    background: var(--orange-deep);
    clip-path: polygon(0 0, 100% 0, 100% 100%, 0 100%, 8px 50%);
    display: flex; align-items: center; justify-content: center;
    flex: none;
  }
  .contact__tab svg { width: 16px; height: 16px; }
  .contact__value {
    width: 330px;
    height: 26px;
    margin-left: 6px;
    background: linear-gradient(180deg, var(--white), #ececec);
    border-radius: 0 14px 14px 0;
    box-shadow: 0 2px 4px rgba(0,0,0,.18);
    display: flex; align-items: center;
    padding-left: 12px;
    color: #333;
    font-size: 17px;
    letter-spacing: .5px;
    white-space: nowrap;
  }
  .person {
    position: absolute;
    left: 450px;
    top: 252px;
    width: 240px;
    text-align: center;
    color: var(--white);
  }
  .person__name {
    font-family: "Michroma", Arial, sans-serif;
    font-size: 16px;
    letter-spacing: 1px;
    white-space: nowrap;
  }
  .person__role { font-size: 16px; margin-top: 6px; letter-spacing: 1px; }
</style>
</head>
<body>

  <section class="card card--back" aria-label="Card back">
    <div class="brand">
      <span class="brand__dot"></span>
      <span class="brand__name">
        <span class="brand__title">VOSSMER</span>
        <span class="brand__sub">COLLECTIVE</span>
      </span>
    </div>
    <p class="tagline">A contributor to Pellham Visuals</p>
  </section>

  <section class="card card--front" aria-label="Card front">
    <svg class="front-art" viewBox="0 0 700 400" preserveAspectRatio="none" aria-hidden="true">
      <defs>
        <linearGradient id="panelOrange" x1="0" y1="0" x2="0" y2="1">
          <stop offset="0" stop-color="#ea6a27"/>
          <stop offset="1" stop-color="#c9301b"/>
        </linearGradient>
      </defs>
      <rect x="0" y="0" width="14" height="400" fill="url(#panelOrange)"/>
      <path d="M700 0 L700 400 L420 400 C440 300 450 200 500 150 C540 110 620 90 700 0 Z" fill="url(#panelOrange)"/>
    </svg>

    <div class="brand">
      <span class="brand__dot"></span>
      <span class="brand__name">
        <span class="brand__title">VOSSMER</span>
        <span class="brand__sub">COLLECTIVE</span>
      </span>
    </div>

    <ul class="contacts">
      <li class="contact">
        <span class="contact__tab">
          <svg viewBox="0 0 16 16"><rect x="4" y="1" width="8" height="14" rx="1.5" fill="none" stroke="#fff" stroke-width="1.6"/><circle cx="8" cy="12.5" r="1" fill="#fff"/></svg>
        </span>
        <span class="contact__value">717 555 0143</span>
      </li>
      <li class="contact">
        <span class="contact__tab">
          <svg viewBox="0 0 16 16"><rect x="1" y="3" width="14" height="10" rx="1" fill="#fff"/><path d="M1.5 3.5 L8 9 L14.5 3.5" fill="none" stroke="#c9321c" stroke-width="1.4"/></svg>
        </span>
        <span class="contact__value">yourmail@inboxmail-example.com</span>
      </li>
      <li class="contact">
        <span class="contact__tab">
          <svg viewBox="0 0 16 16"><circle cx="8" cy="8" r="6.5" fill="none" stroke="#fff" stroke-width="1.5"/><ellipse cx="8" cy="8" rx="3" ry="6.5" fill="none" stroke="#fff" stroke-width="1.2"/><line x1="1.5" y1="8" x2="14.5" y2="8" stroke="#fff" stroke-width="1.2"/></svg>
        </span>
        <span class="contact__value">www.yourweb-example.com</span>
      </li>
    </ul>

    <div class="person">
      <p class="person__name">MORRIS VOSSMER</p>
      <p class="person__role">Founder</p>
    </div>
  </section>

</body>
</html>
```